Post Card (5x7) - Pre-foreclosure Image - Harbor Path Partners

(Two-Sided Post Card)
FACING FORECLOSURE? YOU STILL HAVE OPTIONS.
If you’re behind on payments or at risk of foreclosure, you’re not alone—and it’s not too late to take action.
We help homeowners:
• Explore options to stay in their home
• Stop or delay foreclosure
• Sell quickly for a fair price if needed
No pressure. No obligation. Just real solutions tailored to your situation.
Call - (240) 558-2094
Email - marcus@hpbllc-mail.com
Harbor Path Partners LLC
7200 Bramwick Lane, Ellicott City, MD 21043
**Marcus Fennimore is a Licensed Realtor with Copperleaf Homes Realty in Bethesda, Maryland.
(Leave room for mailing address, return address & postage)
Target Market(s)
Distressed Homeowners
Industry/Entity Type
Real Estate

```html
<!DOCTYPE html>
<html lang="en">
<head>
<meta charset="utf-8">
<title>Harbor Path Partners – Pre-foreclosure Postcard</title>
<link href="https://fonts.googleapis.com/css2?family=Overpass:wght@400;600;700;800&display=swap" rel="stylesheet">
<style>
  :root {
    --backdrop: #7a7a7a;
    --ink: #111111;
    --white: #ffffff;
    --panel-grey: #c4c4c4;
    --divider: #c9c9c9;
    --bar: #050505;
    --sunset-top: #7d7a72;
    --sunset-mid: #a9743a;
    --sunset-low: #2a1c10;
    --dusk-top: #8c6f9a;
    --dusk-mid: #b98a86;
    --dusk-low: #5a3322;
  }
  * { box-sizing: border-box; margin: 0; padding: 0; }
  html, body { width: 1200px; height: 904px; overflow: hidden; }
  body {
    background: var(--backdrop);
    font-family: "Overpass", Arial, sans-serif;
    color: var(--ink);
    position: relative;
  }
  .card {
    position: absolute;
    top: 252px;
    width: 560px;
    height: 400px;
    overflow: hidden;
    box-shadow: 0 6px 18px rgba(0,0,0,.25);
  }
  .card--front { left: 20px; }
  .card--back { left: 620px; background: var(--white); }

  /* Front */
  .front-photo {
    position: absolute; inset: 0 0 54px 0;
    background: linear-gradient(180deg, var(--sunset-top) 0%, var(--sunset-mid) 45%, var(--sunset-low) 80%, #120d08 100%);
  }
  .front-brand {
    position: absolute; left: 24px; top: 60px;
    color: var(--white);
    font-weight: 600; font-size: 15px; letter-spacing: 2.5px;
  }
  .front-headline {
    position: absolute; left: 24px; top: 268px;
    color: var(--white);
    font-weight: 800; font-size: 23px; line-height: 1.28;
    text-transform: uppercase;
  }
  .contact-bar {
    position: absolute; left: 0; right: 0; bottom: 0; height: 54px;
    background: var(--bar); color: var(--white);
    padding: 7px 24px 0;
  }
  .contact-bar__name { font-weight: 700; font-size: 12.5px; text-transform: uppercase; }
  .contact-bar__row { display: flex; align-items: center; gap: 11px; font-size: 11.5px; margin-top: 2px; white-space: nowrap; }
  .contact-item { display: flex; align-items: center; gap: 5px; }
  .icon { width: 12px; height: 12px; flex: none; }

  /* Back */
  .back-message {
    position: absolute; left: 0; top: 0; width: 295px; height: 400px;
  }
  .intro {
    height: 83px; background: var(--panel-grey);
    padding: 22px 24px 0; font-size: 12.6px; line-height: 1.33;
  }
  .services { height: 92px; padding: 10px 24px 0; }
  .services__title { font-weight: 700; font-size: 13px; text-transform: uppercase; margin-bottom: 2px; }
  .services__list { list-style: none; font-size: 12px; }
  .services__list li { display: flex; align-items: center; gap: 6px; height: 17.5px; }
  .back-photo {
    height: 145px;
    background: linear-gradient(180deg, var(--dusk-top) 0%, var(--dusk-mid) 40%, #c27a45 70%, var(--dusk-low) 100%);
  }
  .tagline { height: 41px; padding: 7px 8px 0 24px; font-weight: 700; font-size: 10.5px; letter-spacing: -0.1px; line-height: 1.4; }
  .back-bar {
    height: 39px; background: var(--bar); color: var(--white);
    display: flex; align-items: center; gap: 9px; padding: 0 8px 0 24px;
    font-size: 10.5px; white-space: nowrap;
  }
  .back-bar .phone { font-weight: 700; font-size: 11px; }
  .divider { position: absolute; left: 295px; top: 0; width: 5px; height: 400px; background: var(--divider); }
  .mailing {
    position: absolute; left: 300px; top: 0; width: 260px; height: 400px;
  }
  .return-address { position: absolute; left: 18px; top: 56px; width: 140px; text-align: center; }
  .return-address__name { font-weight: 700; font-size: 11px; letter-spacing: 1.2px; text-transform: uppercase; line-height: 1.25; }
  .return-address__street { font-size: 8px; font-weight: 600; line-height: 1.35; margin-top: 6px; }
  .postage-box {
    position: absolute; right: 24px; top: 24px; width: 62px; height: 59px;
    border: 1.5px solid #d4d4d4;
  }
  .address-line { position: absolute; left: 21px; right: 24px; height: 1px; background: #bdbdbd; }
  .disclaimer { position: absolute; left: 21px; right: 10px; bottom: 16px; font-size: 9.2px; line-height: 1.4; font-weight: 600; }
</style>
</head>
<body>

<section class="card card--front">
  <div class="front-photo" role="img" aria-label="Photo: city skyline at sunset over a river"></div>
  <div class="front-brand">HARBOR PATH PARTNERS</div>
  <h1 class="front-headline">Facing foreclosure?<br>You still have options.</h1>
  <div class="contact-bar">
    <div class="contact-bar__name">Harbor Path Partners LLC</div>
    <div class="contact-bar__row">
      <span class="contact-item">
        <svg class="icon" viewBox="0 0 12 12"><circle cx="6" cy="6" r="6" fill="#fff"/><path d="M6 2.5a2.2 2.2 0 0 0-2.2 2.2C3.8 6.4 6 9.3 6 9.3s2.2-2.9 2.2-4.6A2.2 2.2 0 0 0 6 2.5z" fill="#000"/><circle cx="6" cy="4.7" r=".8" fill="#fff"/></svg>
        7200 Bramwick Lane, Ellicott City, MD 21043
      </span>
      <span class="contact-item">
        <svg class="icon" viewBox="0 0 12 12"><circle cx="6" cy="6" r="6" fill="#fff"/><path d="M4 3l1.1 1.4-.6.8a4 4 0 0 0 2.3 2.3l.8-.6L9 8l-.6 1A4.8 4.8 0 0 1 3 3.6z" fill="#000"/></svg>
        (240) 558-2094
      </span>
      <span class="contact-item">
        <svg class="icon" viewBox="0 0 12 12"><circle cx="6" cy="6" r="6" fill="#fff"/><rect x="3" y="4" width="6" height="4.2" fill="#000"/><path d="M3 4l3 2.2L9 4" stroke="#fff" stroke-width=".7" fill="none"/></svg>
        marcus@hpbllc-mail.com
      </span>
    </div>
  </div>
</section>

<section class="card card--back">
  <div class="back-message">
    <p class="intro">If you’re behind on payments or at risk of foreclosure, you’re not alone—and it’s not too late to take action.</p>
    <div class="services">
      <h2 class="services__title">We help homeowners:</h2>
      <ul class="services__list">
        <li><svg class="icon" viewBox="0 0 12 12"><circle cx="6" cy="6" r="5.5" fill="#000"/><path d="M3.4 6.1l1.8 1.7 3.4-3.5" stroke="#fff" stroke-width="1.4" fill="none"/></svg>Explore options to stay in their home</li>
        <li><svg class="icon" viewBox="0 0 12 12"><circle cx="6" cy="6" r="5.5" fill="#000"/><path d="M3.4 6.1l1.8 1.7 3.4-3.5" stroke="#fff" stroke-width="1.4" fill="none"/></svg>Stop or delay foreclosure</li>
        <li><svg class="icon" viewBox="0 0 12 12"><circle cx="6" cy="6" r="5.5" fill="#000"/><path d="M3.4 6.1l1.8 1.7 3.4-3.5" stroke="#fff" stroke-width="1.4" fill="none"/></svg>Sell quickly for a fair price if needed</li>
      </ul>
    </div>
    <div class="back-photo" role="img" aria-label="Photo: harbor waterfront city buildings at dusk"></div>
    <p class="tagline">No pressure. No obligation. Just real solutions<br>tailored to your situation.</p>
    <div class="back-bar">
      <span class="contact-item phone">
        <svg class="icon" viewBox="0 0 12 12"><circle cx="6" cy="6" r="6" fill="#fff"/><path d="M4 3l1.1 1.4-.6.8a4 4 0 0 0 2.3 2.3l.8-.6L9 8l-.6 1A4.8 4.8 0 0 1 3 3.6z" fill="#000"/></svg>
        (240) 558-2094
      </span>
      <span class="contact-item">
        <svg class="icon" viewBox="0 0 12 12"><circle cx="6" cy="6" r="6" fill="#fff"/><rect x="3" y="4" width="6" height="4.2" fill="#000"/><path d="M3 4l3 2.2L9 4" stroke="#fff" stroke-width=".7" fill="none"/></svg>
        marcus@hpbllc-mail.com
      </span>
    </div>
  </div>
  <div class="divider"></div>
  <div class="mailing">
    <div class="return-address">
      <div class="return-address__name">Harbor Path<br>Partners</div>
      <div class="return-address__street">7200 Bramwick Lane, Ellicott City,<br>MD 21043</div>
    </div>
    <div class="postage-box"></div>
    <div class="address-line" style="top:147px"></div>
    <div class="address-line" style="top:187px"></div>
    <div class="address-line" style="top:224px"></div>
    <p class="disclaimer">**Marcus Fennimore is a Licensed Realtor with<br>Copperleaf Homes Realty in Bethesda, Maryland.</p>
  </div>
</section>

</body>
</html>
```